Tarrow Creek plumbing plumbing company business card design

Something sinilar to business card i upload it is my old business card design
And have a good watermark with the logo or majority of the logot in rhe background as watermark

Plumbing business similar to uploaded design with a nice watermark of the logo

Font styles to use
Script

Colors

Designer to choose colors to be used in the design.

```html
<!DOCTYPE html>
<html lang="en">
<head>
<meta charset="utf-8">
<title>Tarrow Creek Plumbing — Business Card</title>
<link href="https://fonts.googleapis.com/css2?family=Dancing+Script:wght@700&family=Open+Sans:wght@400;600;700&display=swap" rel="stylesheet">
<style>
  :root {
    --backdrop: #2b2b2d;
    --cyan: #00e4f7;
    --blue: #0a7fd0;
    --blue-deep: #0560b5;
    --ink: #050505;
    --paper: #ffffff;
    --accent: #1a8ad8;
    --watermark-light: rgba(255,255,255,.10);
    --watermark-dark: rgba(10,127,208,.07);
  }
  * { margin: 0; padding: 0; box-sizing: border-box; }
  html, body { width: 1200px; height: 885px; overflow: hidden; }
  body {
    background: var(--backdrop);
    font-family: "Open Sans", Arial, sans-serif;
    position: relative;
  }
  .card {
    position: absolute;
    width: 700px;
    height: 400px;
    left: 250px;
    overflow: hidden;
    box-shadow: 0 8px 24px rgba(0,0,0,.45);
  }
  .watermark {
    position: absolute;
    font-family: "Open Sans", Arial, sans-serif;
    font-weight: 700;
    white-space: nowrap;
    line-height: 1;
    pointer-events: none;
    user-select: none;
  }

  /* Front */
  .card-front {
    top: 28px;
    background: linear-gradient(160deg, var(--cyan) 0%, var(--blue) 55%, var(--blue-deep) 100%);
  }
  .card-front .watermark {
    left: -30px;
    top: 40px;
    font-size: 170px;
    color: var(--watermark-light);
    transform: rotate(-12deg);
  }
  .front-brand {
    position: absolute;
    right: 60px;
    bottom: 110px;
    text-align: right;
    color: var(--paper);
  }
  .front-brand .brand-name {
    display: flex;
    align-items: center;
    justify-content: flex-end;
    gap: 14px;
    font-size: 40px;
    font-weight: 700;
    letter-spacing: 1px;
    line-height: 1;
  }
  .brand-dot {
    flex: none;
    width: 22px; height: 22px; border-radius: 50%;
    background: var(--paper);
  }
  .front-brand .web {
    margin-top: 12px;
    font-size: 15px;
  }

  /* Back */
  .card-back {
    top: 457px;
    display: flex;
  }
  .back-info {
    position: relative;
    width: 350px;
    height: 100%;
    background: var(--ink);
    color: var(--paper);
    padding: 62px 24px 0 46px;
  }
  .pipe-band {
    position: absolute;
    left: 0; top: 36px;
    width: 110px; height: 12px;
    background: var(--accent);
  }
  .person-name {
    font-family: "Dancing Script", cursive;
    color: var(--accent);
    font-size: 36px;
    font-weight: 700;
    line-height: 1.1;
  }
  .person-role { font-size: 17px; margin-bottom: 14px; }
  .address { font-size: 15px; line-height: 1.35; margin-bottom: 10px; }
  .contact-list { list-style: none; font-size: 15px; line-height: 1.55; }
  .contact-list li { display: flex; align-items: center; gap: 10px; white-space: nowrap; }
  .contact-list svg { width: 15px; height: 15px; flex: none; fill: var(--accent); }

  .back-brand {
    position: relative;
    width: 350px;
    height: 100%;
    background: var(--paper);
    display: flex;
    align-items: center;
    justify-content: center;
    padding: 0 30px;
  }
  .back-brand .watermark {
    left: -20px;
    top: 120px;
    font-size: 130px;
    color: var(--watermark-dark);
    transform: rotate(-12deg);
  }
  .back-brand .brand-name {
    position: relative;
    display: flex;
    align-items: center;
    gap: 12px;
    color: var(--ink);
    font-size: 24px;
    font-weight: 700;
    letter-spacing: 1px;
    line-height: 1.3;
  }
  .back-brand .brand-dot { background: var(--accent); width: 18px; height: 18px; }
</style>
</head>
<body>
  <section class="card card-front">
    <div class="watermark" aria-hidden="true">TARROW CREEK</div>
    <div class="front-brand">
      <div class="brand-name"><span class="brand-dot"></span>TARROW CREEK</div>
      <div class="web">www.tarrowcreekplumbing.com</div>
    </div>
  </section>

  <section class="card card-back">
    <div class="back-info">
      <span class="pipe-band"></span>
      <h1 class="person-name">Owen Hartley</h1>
      <p class="person-role">President</p>
      <p class="address">412 Bramble Court<br>Millbrook, NY 12545</p>
      <ul class="contact-list">
        <li><svg viewBox="0 0 16 16"><path d="M3 1h3l1 4-2 1a9 9 0 0 0 5 5l1-2 4 1v3a2 2 0 0 1-2 2A13 13 0 0 1 1 3a2 2 0 0 1 2-2z"/></svg>(555) 2184-7730</li>
        <li><svg viewBox="0 0 16 16"><path d="M4 0h8a1 1 0 0 1 1 1v14a1 1 0 0 1-1 1H4a1 1 0 0 1-1-1V1a1 1 0 0 1 1-1zm1 2v10h6V2zm3 11a1 1 0 1 0 0 2 1 1 0 0 0 0-2z"/></svg>(555) 6097-4418</li>
        <li><svg viewBox="0 0 16 16"><path d="M4 1h7v4H4zM1 6h14v7h-3v2H4v-2H1zm4 5v3h6v-3z"/></svg>(555) 3326-9051</li>
        <li><svg viewBox="0 0 16 16"><path d="M0 3h16v10H0zm1 1v1l7 4 7-4V4z"/></svg>info@tarrowcreekplumbing.com</li>
        <li><svg viewBox="0 0 16 16"><circle cx="8" cy="8" r="7"/></svg>www.tarrowcreekplumbing.com</li>
      </ul>
    </div>
    <div class="back-brand">
      <div class="watermark" aria-hidden="true">TARROW</div>
      <div class="brand-name"><span class="brand-dot"></span><span>TARROW CREEK<br>PLUMBING</span></div>
    </div>
  </section>
</body>
</html>
```